South Gulf Cove Post Card advertising my new real estate website

I want to send a postcard to owners in the community of South Gulf Cove Advertising my new website. www.tarrowbendlistings.com This is a page on www.danawhitcomberealty.com I would like to use the home page picture on www.tarrowbendlistings.com as the main big picture and keep the search field on it. on the front of the postcard with my contact info and logo along the bottom of the postcard. On the back of the card I would like to have one side address what is available on the website and include the "how much is your home worth" widget on my webdite along with the Items and I like the check marks for Interactive Map Search, Free Daily Email Updates, Automated Home Searches, Favorite Properties, And Much More. You should be able to find all my logos and contact information on my website or attached below

Target Market(s)

Lot and Homeowners in the community of South Gulf Cove

Industry/Entity Type

Real Estate Agent

Font styles to use
Serif

Colors
0255a3
0592cd
fbed22

Requirements
Must have
• I am a real estate agent - I don't want the front to be too busy just the main page picture and my logos and contact information at the bottom. Also highlighting the www.tarrowbendlistings.com web address prominent on big picture
• use the www.danawhitcomberealty.com web address with contact info at bottom
Nice to have
• This will be mailed so one side of the back of the card should have what I mentioned above regrading home worth widget and check marked features and the other side should be left for mailing purposes. Name logo and return address should be there and for this portion only use the Hemlock Farrow or HF logo as the name of my company and return address will be to Hemlock Farrow Realty

```html
<!DOCTYPE html>
<html lang="en">
<head>
<meta charset="utf-8">
<title>Dana Whitcombe – South Gulf Cove Postcard</title>
<link href="https://fonts.googleapis.com/css2?family=Arimo:wght@400;700&family=Cinzel:wght@600&family=Oswald:wght@600&display=swap" rel="stylesheet">
<style>
  :root{
    --blue:#0255a3;
    --sky:#0592cd;
    --yellow:#fbed22;
    --paper:#ffffff;
    --backdrop:#ececec;
    --ink:#1d2d5c;
    --stamp:#d9d9d9;
  }
  *{box-sizing:border-box;margin:0;padding:0}
  html,body{width:1200px;height:825px;overflow:hidden;background:var(--backdrop)}
  body{position:relative;font-family:"Arimo",Arial,sans-serif;color:var(--ink)}

  .postcard{position:absolute;top:222px;width:570px;height:380px;background:var(--paper);overflow:hidden;box-shadow:0 2px 8px rgba(0,0,0,.12)}
  .postcard--front{left:20px}
  .postcard--back{left:610px}
  .card-art{position:absolute;inset:0}

  /* front */
  .aerial-photo{position:absolute;left:0;top:0;width:570px;height:290px;
    background:linear-gradient(180deg,#8fb3de 0%,#6f93bf 18%,#6d8a86 45%,#5f7a62 70%,#3f5d4e 100%)}
  .search-title{position:absolute;left:150px;top:22px;font-size:21px;font-weight:700;color:#fff;letter-spacing:.2px;white-space:nowrap}
  .site-address{position:absolute;left:258px;top:170px;font-size:19px;font-weight:700;color:var(--yellow);white-space:nowrap;letter-spacing:.2px}
  .search-panel{position:absolute;left:45px;top:62px;width:180px;height:152px;background:rgba(255,255,255,.62);border-radius:4px;padding:7px 8px;font-size:6.5px;color:#2b3a55}
  .field-row{display:flex;gap:10px;margin-bottom:4px;align-items:flex-end}
  .field label{display:block;margin-bottom:1px}
  .select{background:#fff;border:1px solid #9aa6b8;height:11px;border-radius:2px;padding:1px 3px;font-size:6px;position:relative;white-space:nowrap;overflow:hidden}
  .select::after{content:"▾";position:absolute;right:2px;top:0}
  .to{padding-bottom:2px}
  .type-row{display:flex;gap:8px;margin:2px 0 8px}
  .search-btn{display:inline-block;background:var(--blue);color:#fff;font-size:8px;padding:6px 14px;border-radius:3px}
  .advanced{margin-left:12px;text-decoration:underline;color:var(--blue)}
  .agent-badge{position:absolute;left:18px;top:225px;width:88px;height:88px;border-radius:50%;background:#fff;border:5px solid var(--sky)}
  .agent-badge .portrait{position:absolute;inset:6px;border-radius:50%;background:var(--blue)}
  .agent-name{position:absolute;left:8px;top:318px;width:110px;text-align:center;font-size:8.5px;line-height:1.25;white-space:nowrap}
  .agent-name strong{color:var(--blue);display:block}
  .contact-list{position:absolute;left:122px;top:317px;font-size:8px;font-weight:700;color:var(--blue);line-height:1.5;white-space:nowrap}
  .contact-list li{list-style:none;display:flex;align-items:center;gap:4px}
  .contact-list svg,.address svg{width:8px;height:8px;fill:var(--sky);flex:none}
  .address{position:absolute;left:270px;top:317px;font-size:8px;font-weight:700;color:var(--blue);display:flex;gap:4px;line-height:1.5;border-left:1px solid #ccc;padding-left:7px;white-space:nowrap}
  .brand{position:absolute;display:flex;align-items:center;gap:5px;white-space:nowrap}
  .brand-mark{width:11px;height:11px;background:var(--sky);flex:none}
  .brand-name{font-family:"Cinzel",Georgia,serif;font-weight:600;color:var(--blue);line-height:1}
  .brand-title{font-family:"Cinzel",Georgia,serif;font-size:6.5px;color:var(--sky);letter-spacing:1px;position:absolute;white-space:nowrap}
  .front-brand{left:412px;top:322px}
  .front-brand .brand-name{font-size:13px}
  .front-title{left:428px;top:338px}

  /* back */
  .back-brand{left:30px;top:22px}
  .back-brand .brand-name{font-size:17px}
  .back-title{left:48px;top:42px}
  .worth-box{position:absolute;left:20px;top:62px;width:208px;height:120px;border-radius:10px;border:3px solid var(--blue);
    background:linear-gradient(180deg,var(--sky),var(--blue));padding:7px 10px;color:#fff;transform:rotate(4deg)}
  .worth-box h2{font-family:"Oswald",sans-serif;font-weight:600;font-size:11.5px;color:var(--yellow);letter-spacing:.2px;margin-bottom:5px;white-space:nowrap}
  .feature-list li{list-style:none;display:flex;align-items:center;gap:6px;font-size:10.5px;line-height:1.32;white-space:nowrap}
  .feature-list svg{width:9px;height:9px;flex:none}
  .couple-photo{position:absolute;left:25px;top:192px;width:185px;height:148px;
    background:linear-gradient(180deg,#eef2f6 0%,#c9d3dc 55%,#8fa7c6 100%)}
  .partner-badge{position:absolute;top:44px;height:22px;background:#2a2a2a;border-radius:2px}
  .badge-one{left:372px;width:50px}
  .badge-two{left:432px;width:46px;background:#555}
  .stamp-box{position:absolute;left:495px;top:32px;width:52px;height:52px;background:var(--stamp)}
</style>
</head>
<body>

<section class="postcard postcard--front" aria-label="Postcard front">
  <div class="aerial-photo" role="img" aria-label="Aerial photograph of the South Gulf Cove canal community beside the water"></div>
  <h1 class="search-title">South Gulf Cove Real Estate Search</h1>
  <p class="site-address">www.tarrowbendlistings.com</p>

  <form class="search-panel" aria-label="Property search">
    <div class="field-row">
      <div class="field" style="width:75px"><label>City</label><div class="select">Port Charlotte</div></div>
      <div class="field" style="width:75px"><label>Subdivision</label><div class="select">All Subdivisions</div></div>
    </div>
    <div class="field-row">
      <div class="field" style="width:65px"><label>Price</label><div class="select">No Limit</div></div>
      <span class="to">TO</span>
      <div class="field" style="width:65px"><div class="select">No Limit</div></div>
    </div>
    <div class="field-row">
      <div class="field" style="width:32px"><label>Beds</label><div class="select">Any</div></div>
      <div class="field" style="width:32px"><label>Baths</label><div class="select">Any</div></div>
    </div>
    <div>Property Type</div>
    <div class="type-row"><span>☑ Home</span><span>☑ Condo</span><span>☐ Land</span><span>☐ Multi-Fam</span></div>
    <span class="search-btn">Search</span><span class="advanced">Advanced Search</span>
  </form>

  <svg class="card-art" viewBox="0 0 570 380" aria-hidden="true">
    <path d="M0 290 C150 300 380 292 570 255 L570 380 L0 380 Z" fill="var(--paper)"/>
    <path d="M0 283 C170 296 380 285 570 250 L570 262 C380 300 170 308 0 296 Z" fill="var(--blue)"/>
    <path d="M0 278 C170 290 380 279 570 244 L570 250 C380 285 170 296 0 283 Z" fill="var(--sky)"/>
    <rect x="0" y="360" width="570" height="4" fill="var(--yellow)"/>
    <rect x="0" y="364" width="570" height="16" fill="var(--blue)"/>
  </svg>

  <div class="agent-badge"><div class="portrait" role="img" aria-label="Agent portrait"></div></div>
  <p class="agent-name"><strong>Dana Whitcombe</strong>Hemlock Farrow Realty</p>

  <ul class="contact-list">
    <li><svg viewBox="0 0 10 10"><path d="M2 0h2l1 3-1.5 1a6 6 0 0 0 2.5 2.5L7 5l3 1v2a2 2 0 0 1-2 2A8 8 0 0 1 0 2a2 2 0 0 1 2-2z"/></svg>(941) 555-0142</li>
    <li><svg viewBox="0 0 10 10"><circle cx="5" cy="5" r="5"/></svg>www.danawhitcomberealty.com</li>
  </ul>
  <div class="address">
    <svg viewBox="0 0 10 10"><path d="M5 0a3.5 3.5 0 0 1 3.5 3.5C8.5 6 5 10 5 10S1.5 6 1.5 3.5A3.5 3.5 0 0 1 5 0zm0 2a1.5 1.5 0 1 0 0 3 1.5 1.5 0 0 0 0-3z"/></svg>
    <span>118 Harbor Ln. PO Box 212<br>Tarrow Bend, FL 33900</span>
  </div>

  <div class="brand front-brand"><span class="brand-mark"></span><span class="brand-name">Dana Whitcombe</span></div>
  <span class="brand-title front-title">BROKER ASSOCIATE</span>
</section>

<section class="postcard postcard--back" aria-label="Postcard back">
  <svg class="card-art" viewBox="0 0 570 380" aria-hidden="true">
    <path d="M258 0 C300 30 290 90 250 150 C210 215 215 280 270 340 L280 340 C225 280 222 215 262 150 C302 88 312 28 272 0 Z" fill="var(--blue)"/>
    <path d="M246 0 C288 30 278 90 238 150 C198 215 203 280 258 340 L264 340 C210 280 206 215 246 150 C286 90 296 30 254 0 Z" fill="var(--sky)"/>
    <rect x="0" y="340" width="570" height="5" fill="var(--yellow)"/>
    <rect x="0" y="345" width="570" height="35" fill="var(--blue)"/>
  </svg>

  <div class="brand back-brand"><span class="brand-mark"></span><span class="brand-name">Dana Whitcombe</span></div>
  <span class="brand-title back-title">BROKER ASSOCIATE</span>

  <div class="worth-box">
    <h2>HOW MUCH IS YOUR HOME WORTH?</h2>
    <ul class="feature-list">
      <li><svg viewBox="0 0 10 10"><circle cx="5" cy="5" r="5" fill="#fff"/><path d="M2.5 5l1.8 1.8L7.6 3.4" stroke="var(--blue)" stroke-width="1.4" fill="none"/></svg>Interactive Map Search</li>
      <li><svg viewBox="0 0 10 10"><circle cx="5" cy="5" r="5" fill="#fff"/><path d="M2.5 5l1.8 1.8L7.6 3.4" stroke="var(--blue)" stroke-width="1.4" fill="none"/></svg>Free Daily Email Updates</li>
      <li><svg viewBox="0 0 10 10"><circle cx="5" cy="5" r="5" fill="#fff"/><path d="M2.5 5l1.8 1.8L7.6 3.4" stroke="var(--blue)" stroke-width="1.4" fill="none"/></svg>Automated Home Searches</li>
      <li><svg viewBox="0 0 10 10"><circle cx="5" cy="5" r="5" fill="#fff"/><path d="M2.5 5l1.8 1.8L7.6 3.4" stroke="var(--blue)" stroke-width="1.4" fill="none"/></svg>Favorite Properties</li>
      <li><svg viewBox="0 0 10 10"><circle cx="5" cy="5" r="5" fill="#fff"/><path d="M2.5 5l1.8 1.8L7.6 3.4" stroke="var(--blue)" stroke-width="1.4" fill="none"/></svg>And Much More.</li>
    </ul>
  </div>

  <div class="couple-photo" role="img" aria-label="Photograph of a smiling couple holding the keys to their new home"></div>

  <span class="partner-badge badge-one" role="img" aria-label="Partner badge"></span>
  <span class="partner-badge badge-two" role="img" aria-label="Partner badge"></span>
  <div class="stamp-box" aria-label="Stamp area"></div>
</section>

</body>
</html>
```